Novu Staffing Tri Fold Brochure

My company is a recruiting/staffing firm. I need a design that is going to be professional, bright, young, hip and fun. Pictures are key! We want people working in an office, packaging, food production and/or light industrial environment. Must embrace DIVERSITY. Please use the 4 primary colors from the Novu Logo to accent the piece, but not too busy. I am including the content that I would like to be included in the trifold as well as a sample of a trifold I have used in the past in addition to a couple of logos. My website is www.NovuStaffing.example for look and feel.

Target Market(s)

Logistics, Distribution and Manufacturing companies

Industry/Entity Type

Staffing

Requirements
Must have
• Clean, colorful, eye catching, great pictures and graphics. Photo's of diverse people working, in a office, or production setting.
Nice to have
• Must be professional
Should not have
• Not too busy.

```html
<!DOCTYPE html>
<html lang="en">
<head>
<meta charset="utf-8">
<title>Novu Staffing Tri-Fold Brochure</title>
<link rel="stylesheet" href="https://fonts.googleapis.com/css2?family=Montserrat:wght@400;500;600;700;800&display=swap">
<style>
:root{
  --red:#b5121b;
  --green:#1f8a3f;
  --yellow:#e2c21c;
  --ink:#333;
  --muted:#555;
  --page:#ffffff;
  --stage:#e7e7e7;
  --shadow:#bdbdbd;
}
*{box-sizing:border-box;margin:0;padding:0}
html,body{width:1200px;height:4000px;overflow:hidden}
body{background:var(--stage);font-family:"Montserrat",sans-serif;color:var(--ink);position:relative}
.spread{position:absolute;left:50px;width:1100px;height:775px;background:var(--page);overflow:hidden}
.spread-shadow{position:absolute;left:0;width:1040px;height:775px;background:var(--shadow)}
.outside{top:200px}
.outside-shadow{top:260px}
.inside{top:1200px}
.inside-shadow{top:1260px}
.abs{position:absolute}
.photo{position:absolute}
.head{font-weight:700;font-size:15px;letter-spacing:.3px;color:var(--red);text-transform:uppercase;margin-bottom:8px}
.head .tag{color:#fff;padding:1px 4px;margin-right:3px}
.tag.red{background:var(--red)}
.tag.green{background:var(--green)}
.body{font-size:9.6px;line-height:1.48;color:var(--muted);text-align:justify}
.body p{margin-bottom:8px}
.services{list-style:none}
.services li{display:flex;align-items:center;gap:14px;color:#fff;font-weight:600;font-size:16px;margin-bottom:22px;line-height:1.15}
.services svg{width:30px;height:30px;flex:none}
.contacts{font-size:10px;line-height:1.45;color:var(--muted)}
.contacts h4{color:var(--red);font-size:10px;font-weight:700;margin-top:10px}
.contacts h4:first-child{margin-top:0}
.brand{font-weight:700;color:var(--red);font-size:46px;letter-spacing:-1px;line-height:1}
.brand-sub{font-weight:700;color:var(--red);font-size:20px;letter-spacing:1px}
.definition{text-align:center;color:var(--red);font-weight:700;font-size:27px;line-height:1.2}
.definition .accent{color:var(--yellow)}
.def-sub{text-align:center;font-size:12px;color:var(--muted)}
.quote-box{position:relative;border:2px solid #777;border-radius:8px;padding:18px 14px 12px;text-align:center;font-size:12px;line-height:1.4;color:var(--muted)}
.quote-mark{position:absolute;left:50%;top:-22px;transform:translateX(-50%);background:#fff;padding:0 6px;color:var(--green);font-size:34px;font-weight:800;line-height:1}
.option{display:flex;gap:10px;margin-bottom:26px}
.option svg{width:20px;height:20px;flex:none;margin-top:2px}
.option h5{color:var(--red);font-size:12px;font-weight:700;margin-bottom:6px;text-transform:uppercase}
.grid-list{display:grid;list-style:none;column-gap:14px;row-gap:6px;font-size:10px;color:#fff}
.grid-list li::before{content:"";display:inline-block;width:7px;height:7px;border:1.5px solid #fff;border-radius:50%;margin-right:6px;vertical-align:middle}
.band-head{font-weight:700;font-size:15px;color:#fff;text-transform:uppercase;margin-bottom:12px}
.band-head .tag{background:var(--red);color:#fff;padding:1px 5px;margin-right:4px}
.band-head .tag.on-red{background:var(--yellow);color:#fff}
.url-pill{border:2px solid #888;border-radius:16px;padding:5px 16px;font-size:12px;letter-spacing:1.5px;color:var(--muted)}
</style>
</head>
<body>

<div class="spread-shadow outside-shadow"></div>
<section class="spread outside" aria-label="Brochure outside">
  <div class="photo" style="left:0;top:0;width:157px;height:182px;background:linear-gradient(160deg,#5e8f6a,#2f6b45)" role="img" aria-label="Photo of a diverse group of smiling women colleagues with green tint"></div>
  <div class="abs" style="left:180px;top:28px;width:168px">
    <div class="head"><span class="tag red">Our</span>Mission</div>
    <div class="body"><p>At NOVU Staffing, we are passionate in our pursuit to change lives by connecting great people with great organizations.</p></div>
  </div>
  <div class="abs" style="left:40px;top:210px;width:300px">
    <div class="head"><span class="tag green">What</span>We Do</div>
    <div class="body">
      <p>At NOVU Staffing we do things a little differently. We don't just act as a pipeline, blindly pumping workers into your organization who exit almost as quickly as they appear. We provide a system of professional development and training that prepares our talent to enter each placement with the skills and the attitude they need to succeed. In addition to our years of light industrial and professional staffing experience, NOVU Staffing is also a leader in creating client specific onsite programs and high-volume recruitment programs that are designed to meet the specific needs of our individual clients.</p>
      <p>We believe in providing our partners with not only the most prepared talent, but also the most secure. At NOVU Staffing, we do more than simply satisfy the minimum legal requirements for screening. We incorporate an extensive battery of tests and checks, including background and drug, as well as ensuring that every individual we recommend and place is E-Verified.</p>
      <p>NOVU Staffing is powered by a recruiting engine that never stops. With the right combination of passion and process, we not only have the motivation to meet the Temporary Staffing, Temp-to-Hire and Direct Hire needs of great companies, but we also have the resources and experience to deliver on the promise of a better experience. We provide a higher level of service through our on-boarding and pre-training programs, which are designed to maximize the value of our placements.</p>
      <p>At NOVU Staffing, we have a golden opportunity to positively impact the lives of employers and job seekers. This opportunity is a privilege and an honor and is why we love what we do.</p>
      <p>We look forward to learning about your specific needs and exploring how NOVU Staffing can bring immediate and lasting value.</p>
    </div>
  </div>

  <div class="abs" style="left:400px;top:28px;width:300px">
    <div class="head"><span class="tag red">Who</span>We Are</div>
    <div class="body"><p>At NOVU Staffing, we are interested in helping people and improving lives. We partner with great organizations who are looking to make themselves even better by placing driven and passionate individuals interested in improving their lives and careers. NOVU Staffing is a values-based organization that approaches every interaction with integrity and drives to ensure that every placement makes a positive impact.</p></div>
  </div>
  <div class="abs" style="left:367px;top:182px;width:249px;height:334px;background:var(--red);padding:70px 0 0 42px">
    <ul class="services">
      <li><svg viewBox="0 0 30 30" fill="none" stroke="#fff" stroke-width="2"><rect x="4" y="10" width="22" height="14" rx="1"/><path d="M8 10V5h14v5M8 16h14M8 20h10"/></svg>Data<br>Entry</li>
      <li><svg viewBox="0 0 30 30" fill="none" stroke="#fff" stroke-width="2"><circle cx="15" cy="9" r="5"/><path d="M5 27c1-7 5-10 10-10s9 3 10 10M15 17l-2 4 2 6 2-6z"/></svg>Executive<br>Management</li>
      <li><svg viewBox="0 0 30 30" fill="none" stroke="#fff" stroke-width="2"><path d="M15 4v22M8 26h14M6 8h18M6 8l-4 9h8zM24 8l-4 9h8z"/></svg>Legal</li>
      <li><svg viewBox="0 0 30 30" fill="none" stroke="#fff" stroke-width="2"><circle cx="10" cy="9" r="4"/><circle cx="21" cy="11" r="3.5"/><path d="M3 25c0-6 3-9 7-9s7 3 7 9M16 21c1-4 3-6 5-6s5 2 6 7"/></svg>Sales</li>
    </ul>
  </div>
  <div class="abs" style="left:616px;top:182px;width:52px;height:334px;background:var(--yellow)"></div>
  <div class="photo" style="left:668px;top:182px;width:432px;height:334px;background:linear-gradient(135deg,#cfd3d8,#8d96a3 55%,#4d5666)" role="img" aria-label="Photo of a diverse team meeting around an office table"></div>
  <div class="abs contacts" style="left:422px;top:540px;width:200px">
    <h4>NORTH REGION</h4>
    <div>Oakmere – 555-010-1101</div>
    <div>Larkfield – 555-010-1102</div>
    <div>Brindlewood – 555-010-1103</div>
    <div>Harrow Point – 555-010-1104</div>
    <h4>CENTRAL REGION</h4>
    <div>Fenwick Hollow – 555-010-1105</div>
    <h4>EAST REGION</h4>
    <div>Quillbrook – 555-010-1106</div>
    <div>Ashcombe – 555-010-1107</div>
    <h4>SOUTH REGION</h4>
    <div>Redmarsh – 555-010-1108</div>
  </div>

  <div class="abs" style="left:800px;top:48px;width:260px;text-align:center">
    <div class="brand">Novu</div>
    <div class="brand-sub">Staffing</div>
  </div>
  <div class="abs" style="left:745px;top:545px;width:330px">
    <div class="definition">DEFINITION OF<br>NOVU – <span class="accent">VERB</span></div>
    <div class="def-sub" style="margin-top:12px">To be in harmony or accord; To Fit; Agree</div>
    <div class="quote-box" style="margin-top:30px">
      <span class="quote-mark">“</span>
      Yes the candidate meets the requirements, yeah they have the skills, but do they Novu?
    </div>
  </div>
</section>

<div class="spread-shadow inside-shadow"></div>
<section class="spread inside" aria-label="Brochure inside">
  <div class="abs" style="left:40px;top:38px;width:305px">
    <div class="head"><span class="tag green">Staffing</span>Options</div>
    <div class="option">
      <svg viewBox="0 0 20 20" fill="none" stroke="#b5121b" stroke-width="1.6"><circle cx="10" cy="10" r="7.5"/><path d="M10 5v5l3 2"/></svg>
      <div><h5>Temporary</h5><div class="body">This is an ideal solution that provides flexibility for companies that may have projects, seasonal spikes or a need to fill in the gaps when job vacancies occur. It is a great way for companies to ramp up without adding new associates to the payroll. It also saves on associate costs and provides an opportunity to evaluate talent.</div></div>
    </div>
    <div class="option">
      <svg viewBox="0 0 20 20" fill="none" stroke="#b5121b" stroke-width="1.6"><rect x="3" y="4" width="14" height="13" rx="1"/><path d="M3 8h14M7 2v4M13 2v4"/></svg>
      <div><h5>Temp to Hire</h5><div class="body">Is a way for clients to test the waters and see if the candidate will prove themselves and be a good long-term fit with the company. This program enables the client to examine the performance and attitude of the candidate for a predetermined period of time while on NOVU's payroll prior to being offered a full-time position with the client.</div></div>
    </div>
    <div class="option">
      <svg viewBox="0 0 20 20" fill="none" stroke="#b5121b" stroke-width="1.6"><rect x="3" y="7" width="14" height="10" rx="1"/><path d="M7 7V4h6v3M3 11h14"/></svg>
      <div><h5>Direct Hire</h5><div class="body">When a client has a long-term or highly skilled need, direct hire is an ideal program. Many top performers will not leave a full-time job for a temp or temp to hire opportunity. This is a great way for companies to attract top talent. NOVU will recruit and screen candidates to be interviewed with the client. When the client chooses to move forward and offer a full-time position, the candidate will go directly on the client's payroll and become a full-time associate on day 1.</div></div>
    </div>
    <div class="head" style="margin-top:30px"><span class="tag green">Onsite</span>Management</div>
    <div class="body">NOVU Staffing offers Onsite Management for clients that utilize a high volume of NOVU associates. Our Onsite Manager will in essence serve as an extension of our client's management team. They are on the production floor 75% of the time, not in an office. NOVU Staffing's Onsite Manager is charged with training NOVU Associate's, coaching, counseling, driving production as well as quality and overall safety.</div>
  </div>

  <div class="photo" style="left:367px;top:0;width:733px;height:387px;background:linear-gradient(120deg,#6f7683,#b9bfc8 45%,#5b6270)" role="img" aria-label="Photo of a smiling diverse group of office professionals"></div>

  <div class="abs" style="left:367px;top:387px;width:366px;height:262px;background:var(--green);padding:18px 24px">
    <div class="band-head"><span class="tag">Light</span>Industrial</div>
    <ul class="grid-list" style="grid-template-columns:repeat(3,auto)">
      <li>Manufacturing</li><li>Assembly</li><li>Fulfillment</li>
      <li>Logistics</li><li>Printing</li><li>Hospitality</li>
      <li>Packaging</li>
    </ul>
    <div class="band-head" style="margin-top:20px"><span class="tag">Professional</span></div>
    <ul class="grid-list" style="grid-template-columns:repeat(2,auto)">
      <li>Accounting</li><li>Call Center</li>
      <li>Administrative</li><li>Customer Service</li>
      <li>Data Entry</li><li>Executive Management</li>
      <li>Sales</li><li>Legal</li>
    </ul>
  </div>
  <div class="abs" style="left:367px;top:662px;width:366px;text-align:center">
    <div class="brand" style="font-size:34px">Novu</div>
    <div class="brand-sub" style="font-size:13px">Staffing</div>
  </div>
  <div class="abs url-pill" style="left:455px;top:735px">www.NovuStaffing.example</div>

  <div class="abs" style="left:733px;top:387px;width:367px;height:388px;background:var(--red);padding:18px 24px">
    <div class="band-head"><span class="tag on-red">Skilled</span>Trades</div>
    <ul class="grid-list" style="grid-template-columns:repeat(2,auto)">
      <li>Electrical</li><li>C&amp;C Operators/ Programmers</li>
      <li>Maintenance</li><li>Machine Operators</li>
      <li>Welding</li><li>Plumbing</li>
      <li>Painting</li>
    </ul>
  </div>
  <div class="photo" style="left:733px;top:520px;width:367px;height:255px;background:linear-gradient(180deg,rgba(181,18,27,0),#3c3c44 30%,#23232a)" role="img" aria-label="Photo of a diverse group of business people standing together"></div>
</section>

</body>
</html>
```